New Logo and Packaging label for Sweet Chilli Sauce

We need a Logo Design for our business based in Sydney, Australia named Brovalt, and for the first product to launch which will be a Sweet Chilli Sauce. The logo and design has to be scalable to be used for other product additions over time.

The product will be distributed predominantly through growers markets and the web.

We do need a label that goes around a 250ml glass bottle (picture attached) and measures:
15cm tall and
6cm diameter at the widest point

To be included but not be limited to:
‘Brovalt’ logo that is developed
Sweet Chilli Sauce

Hand Made in Australia

250mL

Shake well
Refrigerate after opening

A section for ingredients, bar code and nutrition label

Target Market(s)

Foodies

Industry/Entity Type

Food Production

Logo Text

BROVALT

Colors

Designer to choose colors to be used in the design.

```html
<!DOCTYPE html>
<html lang="en">
<head>
<meta charset="UTF-8">
<title>Brovalt Sweet Chilli Sauce Label</title>
<link rel="stylesheet" href="https://fonts.googleapis.com/css2?family=Marcellus&family=Roboto+Condensed:wght@700&display=swap">
<style>
  :root {
    --page-bg: #f4f4f4;
    --label-black: #1c1b1b;
    --label-charcoal: #2a2828;
    --chilli-red: #e0141b;
    --panel-red: #c4141a;
    --panel-deep: #8c0a0e;
    --gold: #c9a24a;
    --white: #ffffff;
  }
  * { margin: 0; padding: 0; box-sizing: border-box; }
  html, body {
    width: 1200px;
    height: 1200px;
    overflow: hidden;
    background: var(--page-bg);
  }
  .canvas {
    position: relative;
    width: 1200px;
    height: 1200px;
  }
  .label {
    position: absolute;
    left: 340px;
    top: 80px;
    width: 520px;
    height: 1040px;
    background: linear-gradient(90deg, var(--label-black) 0%, var(--label-charcoal) 50%, var(--label-black) 100%);
    overflow: hidden;
  }
  .brand-panel {
    position: absolute;
    left: 48px;
    top: 0;
    width: 427px;
    height: 320px;
    background: radial-gradient(ellipse at 50% 20%, var(--panel-red) 0%, #a80f14 55%, var(--panel-deep) 100%);
    border: 3px solid var(--gold);
    border-top: none;
    display: flex;
    align-items: center;
    justify-content: center;
  }
  .brand-name {
    font-family: "Marcellus", serif;
    font-size: 88px;
    color: var(--white);
    letter-spacing: 1px;
  }
  .product-name {
    position: absolute;
    left: 44px;
    top: 370px;
    font-family: "Marcellus", serif;
    font-size: 96px;
    line-height: 108px;
    color: var(--chilli-red);
    letter-spacing: -2px;
    z-index: 2;
  }
  .chilli-art {
    position: absolute;
    left: 300px;
    top: 345px;
    width: 210px;
    height: 620px;
    border-radius: 40px;
    background: radial-gradient(ellipse at 55% 50%, #d8262b 0%, #9e1418 45%, rgba(42,40,40,0) 75%);
  }
  .volume {
    position: absolute;
    left: 0;
    width: 100%;
    top: 975px;
    text-align: center;
    font-family: "Roboto Condensed", sans-serif;
    font-weight: 700;
    font-size: 28px;
    color: var(--white);
  }
</style>
</head>
<body>
  <div class="canvas">
    <section class="label">
      <div class="brand-panel">
        <span class="brand-name">Brovalt</span>
      </div>
      <div class="chilli-art" role="img" aria-label="Illustration of a red chilli pepper with small wings, a halo and a devil tail"></div>
      <h1 class="product-name">SWEET<br>CHILLI<br>SAUCE</h1>
      <p class="volume">250 ml</p>
    </section>
  </div>
</body>
</html>
```